Toy Company Needs a Web Site For a New Toy

We need a web site for a new toy called "Zippa Roller". The bike is a plastic, non motorized ride on toy for kids ages 1.5 - 5 years of age. The bike is being launched in three colors, red, blue and pink, though we may include a black option too.

For the web site we want something bold and colorful that communicates fun, therefore NO dull colors like black or grey. Nothing too cluttered. We want the site to attract the attention of kids but also give the parents a sense of confidence in our professionalism as a trustworthy toy company. The home page should focus on the bike, with different views of the bike and a small write-up on some of its key features. We would also like the home page to have a video of the bike in play. A obvious link to the shopping basket must be present as well. The site must include a shopping basket and ordering system.

Attached is a screenshot of a site that has the colourfulness and playfulness that we are looking for. Please have a look.

The bike images attached are renderings from the CAD software, actual high res photos will be used when the site is developed.

The product logo is attached and MUST be used on the site. It must be BOLD and can be incorporated into the actual website design.

The site pages are:
Home
Gallery
Buy
Contact

Competitors:
www.brimvalekids.example
www.quorvaride.example
I do not like either of their sites.

We only have one product at this time, so the site is to be focused on that product, not a whole catalog of products. It is really a single product with the ability to purchase.
Updates

Project Deadline Extended
Reason: I am extending this competition in order to give me more time to review each design and provide the feedback that the designers deserve.

Target Market(s)

Parents, children ages 1.5 - 5.

Industry/Entity Type

It Company

Colors
0555a3
eb1f27
9bcb3c
faed22
f78f20
f37022
e34197
a6459a
6b449b

Requirements
Must have
• Please use the logo attached, but feel free to use different colors.
Should not have
• Dull colors like black and grey

```html
<!DOCTYPE html>
<html lang="en">
<head>
<meta charset="utf-8">
<title>Zippa Roller – Home</title>
<link rel="stylesheet" href="https://fonts.googleapis.com/css2?family=Titan+One&family=Alfa+Slab+One&family=Arimo:wght@400;700&display=swap">
<style>
  :root {
    --white: #ffffff;
    --ink: #3a3b3d;
    --nav-blue: #2f9fd6;
    --sky-top: #56afdb;
    --sky-low: #a6d6e4;
    --grass: #86c03b;
    --grass-deep: #6fa92e;
    --red: #c93a2f;
    --red-dark: #8e231c;
    --gold: #e3a600;
    --gold-dark: #b07c00;
    --screen: #212224;
    --screen-icon: #4a4b4e;
    --body-text: #454749;
    --footer-bg: #d7d7d7;
    --footer-line: #c4c4c4;
    --footer-text: #6a6a6a;
  }
  * { margin: 0; padding: 0; box-sizing: border-box; }
  html, body { width: 1200px; height: 992px; overflow: hidden; }
  body { position: relative; font-family: "Arimo", Arial, sans-serif; background: var(--white); }

  .site-header { position: absolute; inset: 0 0 auto 0; height: 88px; background: var(--white); z-index: 3; }
  .brand { position: absolute; left: 82px; top: 26px; display: flex; align-items: center; gap: 8px;
    font-family: "Titan One", sans-serif; font-size: 22px; color: var(--red); text-decoration: none; }
  .brand-dot { width: 28px; height: 28px; border-radius: 50%; background: var(--red); }
  .main-nav { position: absolute; left: 422px; top: 30px; display: flex; align-items: center; gap: 22px;
    font-family: "Titan One", sans-serif; font-size: 22px; letter-spacing: .5px; }
  .main-nav a { text-decoration: none; color: var(--nav-blue); }
  .main-nav a.is-current { color: var(--ink); position: relative; }
  .main-nav a.is-current::after { content: ""; position: absolute; left: 50%; top: 46px; margin-left: -16px;
    border: 12px solid transparent; border-bottom: 10px solid var(--sky-top); border-top: 0; width: 8px; }
  .nav-star { font-size: 11px; color: var(--ink); }

  .btn-buy { position: absolute; display: flex; align-items: center; justify-content: center; gap: 12px;
    background: var(--red); color: var(--white); text-decoration: none; font-family: "Titan One", sans-serif;
    border-radius: 3px; box-shadow: 0 4px 0 var(--red-dark); }
  .btn-buy svg { fill: none; stroke: var(--white); stroke-width: 3; stroke-linecap: round; stroke-linejoin: round; }
  .btn-buy--header { left: 994px; top: 28px; width: 117px; height: 32px; font-size: 21px; }
  .btn-buy--hero { left: 505px; top: 813px; width: 167px; height: 53px; font-size: 32px; }

  .scene { position: absolute; left: 0; top: 88px; width: 1200px; height: 849px;
    background: linear-gradient(180deg, var(--sky-top) 0%, #7cc2de 40%, var(--sky-low) 78%, var(--grass) 82%, var(--grass-deep) 100%); }

  .burst-art { position: absolute; left: 88px; top: 82px; width: 560px; height: 220px; border-radius: 50%;
    background: radial-gradient(ellipse at center, rgba(255,255,255,.85) 0%, rgba(255,255,255,.45) 55%, rgba(255,255,255,0) 72%); }
  .hero-title { position: absolute; left: 178px; top: 306px; font-family: "Titan One", sans-serif; font-size: 56px;
    color: var(--white); line-height: 1; letter-spacing: 1px; }
  .hero-product { position: absolute; left: 180px; top: 368px; font-family: "Alfa Slab One", serif; font-size: 38px;
    color: var(--ink); letter-spacing: 1px; }
  .hero-product .star { font-size: 22px; vertical-align: middle; }

  .video-frame { position: absolute; left: 643px; top: 164px; width: 468px; height: 243px; border: 5px solid var(--white);
    border-radius: 4px; background: var(--screen); display: flex; align-items: center; justify-content: center; }

  .feature-card { position: absolute; left: 162px; top: 462px; width: 510px; height: 329px; background: var(--white);
    border-radius: 6px; box-shadow: 0 5px 0 #c9c9c9; padding: 78px 20px 0 19px; color: var(--body-text);
    font-size: 16.5px; line-height: 26px; }
  .feature-card p { margin-bottom: 10px; }
  .feature-card .lead { font-weight: 700; }
  .feature-card a { color: var(--nav-blue); text-decoration: none; }
  .ribbon { position: absolute; left: 86px; top: 473px; width: 660px; height: 69px; }
  .ribbon-title { position: absolute; left: 125px; top: 473px; width: 582px; height: 52px; display: flex;
    align-items: center; justify-content: center; font-family: "Titan One", sans-serif; font-size: 31px;
    color: var(--white); letter-spacing: .5px; }

  .bike-art { position: absolute; left: 718px; top: 525px; width: 482px; height: 340px; border-radius: 40% 20% 10% 30%;
    background: radial-gradient(ellipse at 55% 50%, #d8d9db 0%, #9c9ea1 55%, rgba(110,112,115,.0) 75%); }

  .site-footer { position: absolute; left: 0; top: 937px; width: 1200px; height: 55px; background: var(--footer-bg);
    border-top: 4px solid var(--footer-line); text-align: center; font-size: 12.5px; line-height: 18px;
    color: var(--footer-text); padding-top: 10px; }
</style>
</head>
<body>
  <header class="site-header">
    <a class="brand" href="#"><span class="brand-dot"></span>Zippa Roller</a>
    <nav class="main-nav">
      <a class="is-current" href="#">HOME</a><span class="nav-star">★</span>
      <a href="#">GALLERY</a><span class="nav-star">★</span>
      <a href="#">CONTACT</a>
    </nav>
    <a class="btn-buy btn-buy--header" href="#">BUY
      <svg width="10" height="14" viewBox="0 0 10 14"><path d="M2 2l5 5-5 5"/></svg></a>
  </header>

  <main class="scene" role="img" aria-label="Cartoon sky with clouds above green hills and a winding road">
  </main>

  <div class="burst-art" role="img" aria-label="Hand-lettered 'Awesome' burst with shooting stars"></div>
  <h1 class="hero-title">NEW COLORFUL</h1>
  <p class="hero-product">ZIPPA <span class="star">★</span> ROLLER <span class="star">★</span></p>

  <div class="video-frame" aria-label="Video of the bike in play">
    <svg width="110" height="110" viewBox="0 0 110 110"><circle cx="55" cy="55" r="50" fill="none" stroke="var(--screen-icon)" stroke-width="5"/><path d="M40 33v44l36-22z" fill="var(--screen-icon)"/></svg>
  </div>

  <section class="feature-card">
    <p class="lead">Vivamus sodales ac odio nec feugiat.</p>
    <p>Lorem ipsum dolor sit amet, consectetur adipiscing elit. Donec ornare metus at lorem lobortis, vitae scelerisque lorem sollicitudin. Phasellus euismod laoreet auctor.</p>
    <p>In auctor nisl vel metus <a href="#">vel nunc.</a> Vulputate tristique. Praesent sagittis sapien libero, quis euismod nisl egestas eget. Aliquam quis risus et ipsum.&nbsp; tempus venenatis sit amet.</p>
  </section>
  <svg class="ribbon" viewBox="0 0 660 69" aria-hidden="true">
    <polygon points="0,16 59,16 59,68 0,68 14,42" fill="var(--gold)"/>
    <polygon points="660,16 601,16 601,68 660,68 646,42" fill="var(--gold)"/>
    <polygon points="39,52 59,68 59,52" fill="var(--gold-dark)"/>
    <polygon points="621,52 601,68 601,52" fill="var(--gold-dark)"/>
    <rect x="39" y="0" width="582" height="52" fill="var(--gold)"/>
  </svg>
  <h2 class="ribbon-title">TRY A SAFE ADVENTURE!</h2>

  <a class="btn-buy btn-buy--hero" href="#">BUY
    <svg width="14" height="22" viewBox="0 0 14 22"><path d="M3 3l8 8-8 8" stroke-width="4"/></svg></a>

  <div class="bike-art" role="img" aria-label="Silver rendering of the ride-on bike standing on the grass"></div>

  <footer class="site-footer">© 2013, Zippa Roller<br>All Rights Reserved</footer>
</body>
</html>
```